Logo / Etikettendesign
Zielgruppe
Renommierte Sektkellerei will neue Wege gehen. Es wird ein neues Produkt kreirt - ein Sekt - der nicht als Sekt wahrgenommen werden soll - sondern als "Lifestyle" Produkt.
Der neue Name des Produktes steht fest "Wolkenzauber"
Aufgabenstellung
Für den Namen "Wolkenzauber" wird ein neues Logo / Schriftzug / Wortbildmarke gesucht, das gleich auf einem Etikett platziert werden soll.
Es kann Perlmutt sein, Es kann bunt sein. schön wäre (nicht unbedingt erforderlich) wenn ein Kussmund dabei wäre. Aber bitte nicht an dem Mund aufhängen. Es kann auch gerne in die Nostalgische Ebene übergehen.
Die Flasche wird dunkelgrün sein.
Es soll später noch ein Rosé in transparenter Flasche dazu kommen.

```html
<!DOCTYPE html>
<html lang="de">
<head>
<meta charset="utf-8">
<title>Wolkenzauber – Jahrgangssekt Etikett</title>
<link rel="stylesheet" href="https://fonts.googleapis.com/css2?family=Cormorant+Garamond:wght@500;600&family=Montserrat:wght@400&display=swap">
<style>
  :root {
    --bottle-green-light: #013a18;
    --bottle-green-dark: #000d05;
    --label-black: #151515;
    --label-charcoal: #2e2e30;
    --gold-light: #f6e3cf;
    --gold-mid: #d8b08c;
    --gold-deep: #9a7256;
    --cream: #f3ebe2;
    --ink: #2a2320;
  }
  html, body {
    margin: 0;
    padding: 0;
    width: 1200px;
    height: 1200px;
    overflow: hidden;
  }
  .canvas {
    width: 1200px;
    height: 1200px;
    background: linear-gradient(225deg, var(--bottle-green-dark) 0%, #02230e 55%, var(--bottle-green-light) 100%);
  }
  .label-art {
    display: block;
    width: 1200px;
    height: 1200px;
  }
  .brand-name {
    font-family: "Cormorant Garamond", "Times New Roman", serif;
    font-weight: 600;
    font-size: 46px;
    letter-spacing: 1px;
  }
  .wine-category {
    font-family: "Montserrat", Arial, sans-serif;
    font-size: 8px;
    letter-spacing: 0.6px;
    fill: var(--gold-light);
  }
  .sweetness {
    font-family: "Cormorant Garamond", "Times New Roman", serif;
    font-weight: 500;
    font-size: 14px;
    fill: var(--ink);
  }
</style>
</head>
<body>
<main class="canvas">
  <svg class="label-art" viewBox="0 0 800 800" xmlns="http://www.w3.org/2000/svg">
    <defs>
      <path id="shield" d="M185,212 C225,190 265,172 305,170 C345,168 375,180 400,188 C425,180 455,168 495,170 C535,172 575,190 615,212 C632,280 632,380 600,460 C560,560 480,610 400,645 C320,610 240,560 200,460 C168,380 168,280 185,212 Z"/>
      <linearGradient id="gold-band" x1="0" y1="0" x2="1" y2="1">
        <stop offset="0" stop-color="var(--gold-light)"/>
        <stop offset="0.5" stop-color="var(--gold-deep)"/>
        <stop offset="1" stop-color="var(--gold-mid)"/>
      </linearGradient>
      <linearGradient id="label-face" x1="0" y1="0" x2="1" y2="0">
        <stop offset="0" stop-color="var(--label-black)"/>
        <stop offset="0.55" stop-color="var(--label-charcoal)"/>
        <stop offset="1" stop-color="var(--label-black)"/>
      </linearGradient>
      <linearGradient id="name-gold" x1="0" y1="0" x2="0" y2="1">
        <stop offset="0" stop-color="#fff4e8"/>
        <stop offset="1" stop-color="var(--gold-mid)"/>
      </linearGradient>
      <linearGradient id="sweetness-band" x1="0" y1="0" x2="1" y2="0">
        <stop offset="0" stop-color="var(--gold-mid)"/>
        <stop offset="0.5" stop-color="var(--cream)"/>
        <stop offset="1" stop-color="var(--gold-mid)"/>
      </linearGradient>
      <linearGradient id="emblem-tone" x1="0" y1="0" x2="0" y2="1">
        <stop offset="0" stop-color="var(--gold-light)" stop-opacity="0.55"/>
        <stop offset="0.7" stop-color="var(--gold-mid)" stop-opacity="0.35"/>
        <stop offset="1" stop-color="var(--gold-deep)" stop-opacity="0.1"/>
      </linearGradient>
      <linearGradient id="flourish-tone" x1="0" y1="0" x2="1" y2="0">
        <stop offset="0" stop-color="var(--gold-mid)" stop-opacity="0.05"/>
        <stop offset="0.5" stop-color="var(--gold-mid)" stop-opacity="0.35"/>
        <stop offset="1" stop-color="var(--gold-mid)" stop-opacity="0.05"/>
      </linearGradient>
    </defs>

    <g class="label">
      <use href="#shield" class="label-edge" fill="#111" transform="translate(400,410) scale(1.02) translate(-400,-410)"/>
      <use href="#shield" class="label-frame" fill="url(#gold-band)" transform="translate(400,410) scale(0.985) translate(-400,-410)"/>
      <use href="#shield" class="label-face" fill="url(#label-face)" transform="translate(400,412) scale(0.955) translate(-400,-412)"/>
      <use href="#shield" class="label-inner-rule" fill="none" stroke="var(--gold-mid)" stroke-width="1" transform="translate(400,414) scale(0.935) translate(-400,-414)"/>
    </g>

    <rect class="kiss-emblem" role="img" aria-label="Kussmund aus goldenen Perlen mit aufsteigenden Perlen darunter"
          x="300" y="205" width="200" height="160" rx="40" fill="url(#emblem-tone)"/>

    <text class="brand-name" x="400" y="417" text-anchor="middle" fill="url(#name-gold)" textLength="322" lengthAdjust="spacingAndGlyphs">WOLKENZAUBER</text>

    <g class="category-line">
      <line x1="258" y1="441" x2="345" y2="441" stroke="var(--gold-deep)" stroke-width="0.8"/>
      <line x1="455" y1="441" x2="540" y2="441" stroke="var(--gold-deep)" stroke-width="0.8"/>
      <text class="wine-category" x="400" y="444" text-anchor="middle">Jahrgangssekt</text>
    </g>

    <rect class="flourish" role="img" aria-label="Goldenes nostalgisches Schnörkelornament"
          x="315" y="488" width="170" height="40" rx="20" fill="url(#flourish-tone)"/>

    <g class="sweetness-band">
      <path d="M290,541 C330,552 470,552 508,541 C490,570 450,595 400,610 C350,595 310,570 290,541 Z" fill="url(#sweetness-band)"/>
      <text class="sweetness" x="400" y="585" text-anchor="middle">trocken</text>
    </g>
  </svg>
</main>
</body>
</html>
```